Brightnest Stays Stationery Design

Letterpaper, business cards, notebook, envelope A4 & A5

Target Market(s)

Business, accommodation, hotels, flexible housing

Font styles to use
Other font styles liked:
• Montserrat

Colors

Designer to choose only greyscale colors for use in the design.

Requirements
Must have
• Luxurious appearance
Keep it simple, just like the logo
Modern
Nice to have
• Tight Luxury Design
Should not have
• Illustrations
Decorative

```html
<!DOCTYPE html>
<html lang="en">
<head>
<meta charset="utf-8">
<title>Brightnest Stays Stationery</title>
<link rel="stylesheet" href="https://fonts.googleapis.com/css2?family=Montserrat:wght@400;500;700&family=Lato:wght@300;400&family=PT+Sans+Narrow&display=swap">
<style>
  :root {
    --backdrop: #d9e4ef;
    --paper: #ffffff;
    --ink: #111111;
    --black: #000000;
    --text-grey: #5e5e5e;
    --body-grey: #555555;
    --bar-grey: #a3a3a6;
    --rule: #9a9a9a;
    --accent-line: #2f3b56;
    --shadow: 0 3px 6px rgba(40, 55, 80, 0.28);
  }
  * { margin: 0; padding: 0; box-sizing: border-box; }
  html, body { width: 1200px; height: 831px; overflow: hidden; }
  body { position: relative; background: var(--backdrop); font-family: "Lato", sans-serif; color: var(--text-grey); }

  .sheet { position: absolute; background: var(--paper); box-shadow: var(--shadow); overflow: hidden; }

  /* brand lockup */
  .brand { position: absolute; display: flex; flex-direction: column; align-items: center; }
  .brand-square { border: 2px solid var(--ink); }
  .brand-name { font-family: "Montserrat", sans-serif; font-weight: 400; color: var(--ink); white-space: nowrap; letter-spacing: 0.08em; }

  /* bottom bars */
  .bar-black, .bar-grey { position: absolute; bottom: 0; }
  .bar-black { left: 0; background: var(--black); }
  .bar-grey { right: 0; background: var(--bar-grey); }

  /* letterhead */
  .letterhead { left: 117px; top: 111px; width: 430px; height: 609px; }
  .letterhead .brand { left: 39px; top: 32px; width: 104px; }
  .letterhead .brand-square { width: 47px; height: 55px; margin-bottom: 10px; }
  .letterhead .brand-name { font-size: 10.5px; }
  .letterhead-contact { position: absolute; left: 305px; top: 46px; font-size: 8px; line-height: 9.6px; color: var(--text-grey); }
  .contact-list { list-style: none; margin-top: 5px; }
  .contact-list li { display: flex; align-items: center; gap: 7px; line-height: 10.8px; }
  .contact-list svg { width: 7px; height: 7px; flex: none; }
  .letter-date { position: absolute; left: 40px; top: 209px; font-family: "Montserrat", sans-serif; font-size: 9px; color: var(--text-grey); }
  .recipient-name { position: absolute; left: 40px; top: 225px; font-family: "Montserrat", sans-serif; font-weight: 700; font-size: 14.5px; color: var(--text-grey); }
  .recipient-title { position: absolute; left: 40px; top: 246px; font-size: 9.8px; color: var(--text-grey); }
  .letter-body { position: absolute; left: 40px; top: 287px; width: 351px; font-family: "PT Sans Narrow", sans-serif; font-size: 8.5px; line-height: 15px; color: var(--body-grey); text-align: justify; }
  .letter-body p + p { margin-top: 15px; }
  .sign-off { position: absolute; left: 40px; top: 452px; font-family: "PT Sans Narrow", sans-serif; font-size: 9.6px; color: var(--body-grey); }
  .signature { position: absolute; left: 40px; top: 476px; width: 46px; height: 30px; background: #e9e9e9; }
  .letterhead .bar-black { width: 354px; height: 6px; }
  .letterhead .bar-grey { width: 74px; height: 6px; }

  /* business card front */
  .card-front { left: 636px; top: 113px; width: 182px; height: 104px; }
  .card-front .brand { left: 122px; top: 11px; width: 48px; }
  .card-front .brand-square { width: 21px; height: 25px; border-width: 1px; margin-bottom: 4px; }
  .card-front .brand-name { font-size: 5px; }
  .card-holder { position: absolute; left: 11px; top: 50px; }
  .card-holder-name { font-family: "Montserrat", sans-serif; font-weight: 700; font-size: 8.2px; color: var(--ink); }
  .card-holder-role { font-size: 4.4px; color: var(--text-grey); margin-top: 1px; }
  .card-rule { position: absolute; left: 11px; right: 11px; top: 69px; height: 0; border-top: 0.6px solid var(--rule); }
  .card-contact { position: absolute; left: 11px; top: 73px; list-style: none; font-size: 4.4px; color: var(--text-grey); }
  .card-contact li { display: flex; align-items: center; gap: 4px; line-height: 6.7px; }
  .card-contact svg { width: 4px; height: 4px; }
  .card-address { position: absolute; right: 11px; top: 79px; text-align: right; font-size: 4.4px; line-height: 7px; color: var(--text-grey); }
  .card-front .bar-black { width: 150px; height: 4px; }
  .card-front .bar-grey { width: 31px; height: 4px; }

  /* business card back */
  .card-back { left: 904px; top: 111px; width: 183px; height: 104px; background: var(--black); }
  .card-back .brand { left: 0; right: 0; top: 25px; }
  .card-back .brand-square { width: 29px; height: 34px; border-color: var(--paper); border-width: 1.5px; margin-bottom: 7px; }
  .card-back .brand-name { font-size: 8px; color: var(--paper); }

  /* envelope back */
  .envelope-back { left: 636px; top: 248px; width: 451px; height: 226px; }
  .envelope-flap { position: absolute; left: 0; top: 0; width: 451px; height: 66px; }

  /* envelope front */
  .envelope-front { left: 636px; top: 494px; width: 451px; height: 226px; }
  .envelope-front .brand { left: 40px; top: 35px; width: 96px; }
  .envelope-front .brand-square { width: 41px; height: 48px; margin-bottom: 8px; }
  .envelope-front .brand-name { font-size: 9.4px; }
  .return-address { position: absolute; left: 44px; top: 171px; padding-left: 8px; border-left: 1px solid var(--accent-line); font-size: 9.6px; line-height: 11.6px; color: var(--text-grey); }
  .envelope-front .bar-black { width: 370px; height: 6px; }
  .envelope-front .bar-grey { width: 77px; height: 6px; }
</style>
</head>
<body>

  <!-- Letterhead -->
  <section class="sheet letterhead">
    <div class="brand">
      <div class="brand-square"></div>
      <span class="brand-name">BRIGHTNEST STAYS</span>
    </div>

    <div class="letterhead-contact">
      <div>1234 First Line Address<br>5678 Second Line Address</div>
      <ul class="contact-list">
        <li><svg viewBox="0 0 10 10"><path d="M2 1 L4 1 L4.6 3.4 L3.4 4.2 Q4.4 6 5.8 6.6 L6.6 5.4 L9 6 L9 8 Q8.6 9 7.6 9 Q1 8.4 1 2.4 Q1 1 2 1Z" fill="#222"/></svg>(555) 214-3080</li>
        <li><svg viewBox="0 0 10 10"><rect x="0.5" y="2" width="9" height="6" fill="#222"/><path d="M0.5 2 L5 5.5 L9.5 2" stroke="#fff" stroke-width="0.8" fill="none"/></svg>hello@brightneststays.com</li>
        <li><svg viewBox="0 0 10 10"><circle cx="5" cy="5" r="4.2" fill="none" stroke="#222" stroke-width="0.9"/><ellipse cx="5" cy="5" rx="1.8" ry="4.2" fill="none" stroke="#222" stroke-width="0.7"/><path d="M1 5 H9 M1.6 3 H8.4 M1.6 7 H8.4" stroke="#222" stroke-width="0.6"/></svg>www.brightneststays.com</li>
      </ul>
    </div>

    <p class="letter-date">01 December, 2021</p>
    <h1 class="recipient-name">DANIEL HART</h1>
    <p class="recipient-title">Cheif Executive Officer</p>

    <div class="letter-body">
      <p>Contrary to popular belief, Lorem Ipsum is not simply random text. It has roots in a piece of classical Latin literature from 45 BC, making it over 2000 years old. Harold Winslow, a Latin professor at Ashford Hill College in Vermont, looked up one of the more obscure Latin words, consectetur.</p>
      <p>Lorem Ipsum comes from sections 1.10.32 and 1.10.33 of "de Finibus Bonorum et Malorum" (The Extremes of Good and Evil) by Aurelian Sextus, written in 45 BC. This book is a treatise on the theory of ethics, very popular during the Renaissance. The first line of Lorem Ipsum.</p>
      <p>The standard chunk of Lorem Ipsum used since the 1500s is reproduced below for those interested.</p>
    </div>

    <p class="sign-off">Best Regards</p>
    <div class="signature" role="img" aria-label="Handwritten signature of the sender"></div>

    <div class="bar-black"></div>
    <div class="bar-grey"></div>
  </section>

  <!-- Business card, front -->
  <section class="sheet card-front">
    <div class="brand">
      <div class="brand-square"></div>
      <span class="brand-name">BRIGHTNEST STAYS</span>
    </div>
    <div class="card-holder">
      <p class="card-holder-name">OWEN REYES</p>
      <p class="card-holder-role">Founder &amp; CEO</p>
    </div>
    <div class="card-rule"></div>
    <ul class="card-contact">
      <li><svg viewBox="0 0 10 10"><path d="M2 1 L4 1 L4.6 3.4 L3.4 4.2 Q4.4 6 5.8 6.6 L6.6 5.4 L9 6 L9 8 Q8.6 9 7.6 9 Q1 8.4 1 2.4 Q1 1 2 1Z" fill="#222"/></svg>(555) 214-3080</li>
      <li><svg viewBox="0 0 10 10"><rect x="0.5" y="2" width="9" height="6" fill="#222"/></svg>hello@brightneststays.com</li>
      <li><svg viewBox="0 0 10 10"><circle cx="5" cy="5" r="4.2" fill="none" stroke="#222" stroke-width="1.2"/></svg>www.brightneststays.com</li>
    </ul>
    <div class="card-address">1234 First Line Address<br>5678 Second Line Address</div>
    <div class="bar-black"></div>
    <div class="bar-grey"></div>
  </section>

  <!-- Business card, back -->
  <section class="sheet card-back">
    <div class="brand">
      <div class="brand-square"></div>
      <span class="brand-name">BRIGHTNEST STAYS</span>
    </div>
  </section>

  <!-- Envelope, back -->
  <section class="sheet envelope-back">
    <svg class="envelope-flap" viewBox="0 0 451 66" aria-hidden="true">
      <path d="M0 0 H451 L446 40 Q443 66 414 66 H36 Q9 66 5 40 Z" fill="#000"/>
      <rect x="209" y="20" width="12" height="14" fill="none" stroke="#fff" stroke-width="1"/>
      <text x="226" y="30.5" font-family="Montserrat, sans-serif" font-size="7" fill="#fff" letter-spacing="0.6">BRIGHTNEST STAYS</text>
    </svg>
  </section>

  <!-- Envelope, front -->
  <section class="sheet envelope-front">
    <div class="brand">
      <div class="brand-square"></div>
      <span class="brand-name">BRIGHTNEST STAYS</span>
    </div>
    <div class="return-address">1234 First Line Address<br>5678 Second Line Address</div>
    <div class="bar-black"></div>
    <div class="bar-grey"></div>
  </section>

</body>
</html>
```